Business Card Design using new logo

As much as we'd like to think that treating everyone equally is the best strategy for fairness, the reality is that the differences in the lives of women and men have to be taken into account to ensure that organizations, programs, services, and yes, even public policy treat women and men in ways that achieve gender equity.

That's where ParityLoom - balance insight metrics comes in. Using the data-driven tools of gender analysis, our organization can help anyone determine if gender equity is being achieved - in businesses and organizations, in the planning and implementation of programs and services, and in the development and enforcement of public policy.
Updates

Apologies for the delay - have not had time to finalize the decision.  Should be early this week - probably Tuesday.

Industry/Entity Type

Business

Requirements
Must have
• New Logo for ParityLoom
• Logo plus words "Balance Insight Metrics"

```html
<!DOCTYPE html>
<html lang="en">
<head>
<meta charset="utf-8">
<title>ParityLoom Business Card</title>
<link rel="stylesheet" href="https://fonts.googleapis.com/css2?family=Questrial&family=Open+Sans:wght@400&display=swap">
<style>
  :root {
    --stage: #ebe8e6;
    --card-white: #ffffff;
    --brand-orange: #f59a36;
    --ink-dark: #3a3a3a;
    --ink-mid: #6b6b6b;
    --ink-light: #9a9a9a;
    --card-shadow: rgba(0, 0, 0, 0.14);
  }
  * { box-sizing: border-box; margin: 0; padding: 0; }
  html, body {
    width: 1200px; height: 997px; overflow: hidden;
    background: var(--stage);
  }
  .stage { position: relative; width: 1200px; height: 997px; }
  .card {
    position: absolute;
    width: 540px; height: 309px;
    box-shadow: 0 8px 24px var(--card-shadow);
  }

  /* Front side */
  .card--front { left: 70px; top: 150px; background: var(--card-white); }
  .card-tagline {
    position: absolute; top: 14px; right: 20px;
    font: 400 11px "Questrial", sans-serif; color: var(--ink-light);
  }
  .brand {
    position: absolute; display: flex; align-items: center; gap: 10px;
    font-family: "Questrial", sans-serif;
  }
  .brand-dot { border-radius: 50%; background: var(--brand-orange); flex: none; }
  .card--front .brand { left: 32px; top: 100px; }
  .card--front .brand-dot { width: 30px; height: 30px; }
  .card--front .brand-name { font-size: 32px; color: var(--ink-dark); }

  .holder { position: absolute; right: 22px; top: 74px; text-align: right; font-family: "Questrial", sans-serif; }
  .holder-name { font-size: 21px; color: var(--ink-dark); }
  .holder-role { font-size: 15px; color: var(--ink-mid); margin-top: 2px; }

  .contact {
    position: absolute; left: 40px; bottom: 26px; list-style: none;
    font: 400 11.5px/1.5 "Open Sans", sans-serif; color: var(--ink-dark);
  }
  .contact li { display: flex; align-items: flex-start; gap: 7px; }
  .contact svg { width: 11px; height: 11px; margin-top: 3px; flex: none; fill: var(--brand-orange); }

  /* Back side */
  .card--back { left: 590px; top: 520px; background: var(--brand-orange); }
  .card--back .brand { left: 50%; top: 96px; transform: translateX(-50%); }
  .card--back .brand-dot { width: 48px; height: 48px; background: var(--card-white); }
  .card--back .brand-name { font-size: 46px; color: var(--card-white); }
  .card--back .card-subtitle {
    position: absolute; left: 0; right: 0; top: 188px; text-align: center;
    font: 400 20px "Questrial", sans-serif; color: var(--card-white); letter-spacing: 0.5px;
  }
</style>
</head>
<body>
<main class="stage">

  <section class="card card--front" aria-label="Business card front">
    <p class="card-tagline">Balance Insight Metrics</p>
    <div class="brand">
      <span class="brand-dot"></span>
      <span class="brand-name">ParityLoom</span>
    </div>
    <div class="holder">
      <p class="holder-name">Marcus Hale</p>
      <p class="holder-role">Executive</p>
    </div>
    <ul class="contact">
      <li>
        <svg viewBox="0 0 12 12" aria-hidden="true"><path d="M6 1 L11 6 H9.5 V11 H7 V8 H5 V11 H2.5 V6 H1 Z"/></svg>
        <span>Level 2, 48 Kauri St, P O Box 302<br>Waimarie 6120</span>
      </li>
      <li>
        <svg viewBox="0 0 12 12" aria-hidden="true"><path d="M1 2.5 H11 V9.5 H1 Z M1.6 3 L6 6.5 L10.4 3" fill="none" stroke="#f59a36" stroke-width="1.2"/></svg>
        <span>m.hale@parityloom.com</span>
      </li>
      <li>
        <svg viewBox="0 0 12 12" aria-hidden="true"><path d="M2.5 1 L4.5 1 L5.3 3.6 L4 4.6 C4.7 6 6 7.3 7.4 8 L8.4 6.7 L11 7.5 L11 9.5 C11 10.3 10.3 11 9.5 11 C5 11 1 7 1 2.5 C1 1.7 1.7 1 2.5 1 Z"/></svg>
        <span>0455 218 930</span>
      </li>
      <li>
        <svg viewBox="0 0 12 12" aria-hidden="true"><g fill="none" stroke="#f59a36" stroke-width="1"><circle cx="6" cy="6" r="4.8"/><ellipse cx="6" cy="6" rx="2" ry="4.8"/><path d="M1.2 6 H10.8"/></g></svg>
        <span>parityloom.com</span>
      </li>
    </ul>
  </section>

  <section class="card card--back" aria-label="Business card back">
    <div class="brand">
      <span class="brand-dot"></span>
      <span class="brand-name">ParityLoom</span>
    </div>
    <p class="card-subtitle">Balance Insight Metrics</p>
  </section>

</main>
</body>
</html>
```